Bellbird Crossing Roadhouse Take-away Menu

Looking for a menu that is for a popular local roadhouse, we have fuel, take-away food, grocery's and local produce. Our target markets are locals, truck and bus drivers and holiday makers. I have attached logo and a layout mock up that I did and some menu lists

Target Market(s)

truck drivers, tourists, locals - 18-75 years, male and female, budget consious

Industry/Entity Type

Fast Food Restaurant

Colors
ec1f27
3176b5
33a6d7

Requirements
Must have
• Promote Off Road plenty of parking
• Promote Veltro Fuel including premium 98 Unleaded and Steady Burn Diesel
• Feature different headings of drinks menu, box specials, burgers and sandwiches, breakfast, fry up and opening hours
• Feature the logo,
• A5 folded landscape double sided
Nice to have
• I like the american roadhouse type style, easy to read, I like the rust, country, outback type themes
Should not have
• Fancy hard to read writing

```html
<!DOCTYPE html>
<html lang="en">
<head>
<meta charset="utf-8">
<title>Bellbird Crossing Roadhouse – Take Away Menu</title>
<link href="https://fonts.googleapis.com/css2?family=Oswald:wght@400;600&family=Roboto+Condensed:wght@400;700&display=swap" rel="stylesheet">
<style>
:root{
  --red:#ec1f27;
  --blue:#3176b5;
  --sky:#33a6d7;
  --ink:#1a1a1a;
  --paper:#eef0ee;
  --steel:#aeb8c4;
  --bg:#e4e0dc;
}
*{box-sizing:border-box;margin:0;padding:0}
html,body{width:1200px;height:900px;overflow:hidden;background:var(--bg)}
body{font-family:"Roboto Condensed",Arial,sans-serif;color:var(--ink);position:relative}
.head{font-family:"Oswald",Impact,sans-serif;text-transform:uppercase;letter-spacing:.5px}

.spread{position:absolute;left:285px;width:630px;height:438px;display:flex;box-shadow:0 2px 6px rgba(0,0,0,.25)}
.spread.outside{top:6px}
.spread.inside{top:456px}
.panel{position:relative;width:315px;height:100%;overflow:hidden;
  background:linear-gradient(180deg,#c7302b 0,#b86d6a 10%,#b3b5bf 24%,#b0bac6 70%,#8396aa 100%)}
.panel+.panel{border-left:1px solid rgba(0,0,0,.25)}

/* drinks */
.card{position:absolute;background:var(--paper);box-shadow:0 1px 3px rgba(0,0,0,.3)}
.bar-title{background:var(--red);color:#fff;font-size:13px;padding:3px 10px;white-space:nowrap}
.drinks{left:12px;top:18px;width:291px;padding-bottom:6px}
.drink{display:flex;justify-content:space-between;align-items:flex-end;border-bottom:1px solid #777;margin:0 8px;padding:4px 0 2px}
.drink b{font-size:8.5px;font-weight:400;text-transform:uppercase;display:block}
.drink small{font-size:6px;display:block}
.drink .price{font-size:8.5px;font-weight:700}
.map{position:absolute;left:14px;top:290px;width:92px;height:92px;border-radius:50% 50% 50% 0;transform:rotate(-45deg);background:#e8ecee;border:6px solid var(--red)}
.hours{left:122px;top:286px;width:178px;height:112px;background:var(--sky);text-align:center;padding:6px;color:#fff}
.hours .head{font-size:8px;line-height:1.35}
.hours .open{color:var(--red);font-size:9px}
.hours .note{color:var(--red);font-size:7.5px;font-style:italic;margin:3px 0}
.address{position:absolute;left:58px;top:410px;font-size:7px}

/* cover */
.brand{position:absolute;left:12px;top:18px;display:flex;align-items:center;gap:6px}
.brand .mark{width:14px;height:14px;background:var(--blue)}
.brand span{font-family:"Oswald",sans-serif;font-size:10px;color:#fff;text-transform:uppercase;width:70px;line-height:1.2}
.cover-title{position:absolute;left:118px;top:12px;color:var(--blue);font-size:27px;line-height:1;text-align:center;width:150px}
.band{position:absolute;left:0;top:88px;width:315px;height:58px;background:#111;color:#fff}
.car{position:absolute;left:6px;top:8px;width:86px;height:40px;background:linear-gradient(180deg,#4a4a4a,#222);border-radius:18px 24px 6px 6px}
.band .head{position:absolute;right:8px;text-align:right;font-size:15px;line-height:1.25;top:6px}
.photo{position:absolute;right:0;top:146px;width:58px;height:230px;background:linear-gradient(180deg,#6aa6d8,#9c7a5a 55%,#7d5b3e)}
.fuel{position:absolute;left:10px;top:160px;width:240px;text-align:center;font-size:19px;line-height:1.35}
.phone{position:absolute;left:80px;top:404px;font-family:"Oswald",sans-serif;font-size:15px;display:flex;align-items:center;gap:4px}

/* inside left */
.boxes{left:12px;top:18px;width:291px;padding-bottom:5px}
.boxes .bar-title{font-size:9px}
.box-row{display:flex;justify-content:space-between;border:1px solid var(--sky);margin:3px 6px 0;padding:1px 3px;font-size:5.5px}
.box-row b{color:var(--red);font-weight:700;font-size:6px;margin-right:3px}
.breakfast{left:12px;top:120px;width:108px;height:140px;background:var(--sky);color:#fff}
.breakfast .bar-title{background:#111;font-size:10px;padding:2px 6px}
.breakfast .bar-title small{font-size:5px;letter-spacing:0}
.bf{padding:4px 6px 0;font-size:6px;display:flex;justify-content:space-between;gap:3px}
.bf small{display:block;font-size:4.8px;opacity:.9}
.special{left:14px;top:272px;width:104px;padding:8px 6px;text-align:center;transform:rotate(-3deg)}
.special .head{color:var(--red);font-size:8px;line-height:1.3}
.special .goodies{font-family:Georgia,serif;font-size:6.5px;line-height:1.5;margin-top:4px}
.fryup{left:128px;top:112px;width:178px;height:316px}
.fryup .bar-title{font-size:9px}
.fry{display:flex;justify-content:space-between;font-size:5.5px;margin:0 8px;border-bottom:1px dotted #999;padding:1.2px 0;text-transform:uppercase}

/* burgers */
.burgers{left:10px;top:18px;width:295px;height:410px}
.burgers .bar-title{font-size:11px;text-align:right}
.burger{display:flex;justify-content:space-between;align-items:flex-end;margin:0 10px;border-bottom:1px dotted #777;padding:2.5px 0 1px}
.burger b{font-size:8px;font-weight:400;text-transform:uppercase;display:block}
.burger small{font-size:5.6px;display:block}
.burger .price{font-size:7.5px;font-weight:700}
</style>
</head>
<body>

<section class="spread outside">
  <div class="panel drinks-panel">
    <div class="card drinks">
      <h2 class="bar-title head">Drinks Menu</h2>
      <div class="drink"><div><b>Local Ridgeline Coffee</b></div></div>
      <div class="drink"><div><b>Redgum Leaf Local Tea</b><small>Earl grey, English breakfast, peppermint</small></div></div>
      <div class="drink"><div><b>Redgum Leaf Wet Chai</b><small>Brewed in soy milk &nbsp; SMALL $3.50 &nbsp; MEDIUM $4.00 &nbsp; LARGE $4.50</small></div></div>
      <div class="drink"><div><b>Milkshakes or Thick Shakes</b><small>chocolate, banana, or strawberry, coffee</small></div><span class="price">$5.50</span></div>
      <div class="drink"><div><b>Morning Sunrise Juice</b><small>Orange, pineapple, &amp; mint</small></div><span class="price">$5.50</span></div>
      <div class="drink"><div><b>Iced Coffee &amp; Iced Chocolate</b><small>Earl grey, English breakfast, peppermint</small></div><span class="price">$5.50</span></div>
      <div class="drink"><div><b>Fancy Pants Shakes</b><small>best served in house S'more sensation Choc Wafer Kitty (contains coffee)</small><small>Chai and coconut made in heaven</small></div><span class="price">$9.50</span></div>
    </div>
    <div class="map" role="img" aria-label="Location map of the roadhouse on the highway"></div>
    <div class="card hours">
      <p class="head open">Open 7 Days</p>
      <p class="head">Mon—Saturday: 7am—8:30pm</p>
      <p class="head">Sunday 7:30am – 5:30pm</p>
      <p class="note">Please place dinner orders before 6pm for pickup. Kitchen open 6am – 8pm</p>
      <p class="head" style="font-size:7px">We look forward to seeing you!</p>
    </div>
    <p class="address">Lot 3 Outback Hwy, Bellbird NT 0870, Australia</p>
  </div>

  <div class="panel cover">
    <div class="brand"><div class="mark"></div><span>Bellbird Crossing Roadhouse</span></div>
    <h1 class="cover-title head">Take Away Menu</h1>
    <div class="band">
      <div class="car" role="img" aria-label="Illustration of a vintage car"></div>
      <p class="head">Off Street<br>Plenty of Parking!</p>
    </div>
    <div class="photo" role="img" aria-label="Photos of the roadhouse forecourt and building"></div>
    <p class="fuel head">Veltro Fuel<br>Including Premium<br>98 Unleaded<br>&amp;<br>Steady Burn Diesel</p>
    <p class="phone">
      <svg width="12" height="12" viewBox="0 0 24 24"><path fill="#1a1a1a" d="M6.6 10.8a15 15 0 006.6 6.6l2.2-2.2c.3-.3.7-.4 1-.2 1.1.4 2.3.6 3.6.6.6 0 1 .4 1 1V20c0 .6-.4 1-1 1A17 17 0 013 4c0-.6.4-1 1-1h3.5c.6 0 1 .4 1 1 0 1.3.2 2.5.6 3.6.1.3 0 .7-.2 1z"/></svg>
      61 8 8900 4417
    </p>
  </div>
</section>

<section class="spread inside">
  <div class="panel food-panel">
    <div class="card boxes">
      <h2 class="bar-title head">Local Box Specials</h2>
      <div class="box-row"><span><b>WALLY BOX</b>chips, chicken schnitzel, cheese, bacon, onion &amp; gravy</span><span>$13</span></div>
      <div class="box-row"><span><b>CUTLETS BOX</b>2 lamb cutlets, chips, gravy</span><span>$14</span></div>
      <div class="box-row"><span><b>FISH BOX</b>2 flathead fillets, chips, lemon wedge, tartare sauce</span><span>$14</span></div>
      <div class="box-row"><span><b>OUT OF THE OCEAN</b>2 barra bites, 4 prawn cutlets, 4 calamari, 4 flathead fillets, seafood sticks, chips</span><span>$28.50</span></div>
      <div class="box-row"><span><b>ROAD HOUSE RIOLETS</b>2 chicken wings, chips, sauce, rice and a fried egg</span><span>$16</span></div>
    </div>

    <div class="card breakfast">
      <h2 class="bar-title head">Breakfast <small>(served all day)</small></h2>
      <div class="bf"><span>BULLDOZER BREAKY BURGER<small>Beef, bacon, egg, cheese, hash brown</small></span><span>$12.50</span></div>
      <div class="bf"><span>BACON AND EGG ROLL<small>Bacon, egg and sauce on a roll</small></span><span>$8.00</span></div>
      <div class="bf"><span>BACON BREAKY WRAP<small>Bacon, egg, cheese, hash brown</small></span><span>$7.50</span></div>
      <div class="bf"><span>BELLBIRD BREAKY<small>Eggs, bacon, sausage, toast, beans</small></span><span>$13</span></div>
      <div class="bf"><span>B.L.T</span><span>$8.50</span></div>
    </div>

    <div class="card special">
      <p class="head">Check the daily special board for all sorts of goodies including</p>
      <p class="goodies">Homemade pies &amp; sausage rolls<br>Moroccan chicken<br>&amp; plain meat lasagne<br>Fresh Sushi</p>
    </div>

    <div class="card fryup">
      <h2 class="bar-title head">Roadhouse Fry Up</h2>
      <div class="fry"><span>Calamari</span><span>$8.90</span></div>
      <div class="fry"><span>Chicken &amp; garlic balls</span><span>$1.50</span></div>
      <div class="fry"><span>Chicken bust</span><span>$4.00</span></div>
      <div class="fry"><span>Chicken schnitzel only</span><span>$8.00</span></div>
      <div class="fry"><span>Chicken tenders - salt and vinegar</span><span>$2.00</span></div>
      <div class="fry"><span>Chicken tenders - sweet chilli</span><span>$2.00</span></div>
      <div class="fry"><span>Chicken wedges</span><span>$3.00</span></div>
      <div class="fry"><span>Chicken wing dings</span><span>$2.80</span></div>
      <div class="fry"><span>Veggie roll</span><span>$3.90</span></div>
      <div class="fry"><span>Dim sims - on oven</span><span>$2.00</span></div>
      <div class="fry"><span>Dim sims - normal - steamed</span><span>$1.60</span></div>
      <div class="fry"><span>Dim sims - vegetable</span><span>$1.80</span></div>
      <div class="fry"><span>Fish cakes</span><span>$2.50</span></div>
      <div class="fry"><span>Fish fillets</span><span>$4.00</span></div>
      <div class="fry"><span>Kransky sausage</span><span>$3.50</span></div>
      <div class="fry"><span>Lamb cutlet</span><span>$6.00</span></div>
      <div class="fry"><span>Pie - cheese &amp; bacon</span><span>$5.20</span></div>
      <div class="fry"><span>Pie - chunky steak</span><span>$5.20</span></div>
      <div class="fry"><span>Battered sav</span><span>$3.00</span></div>
      <div class="fry"><span>Potato cake</span><span>$1.60</span></div>
      <div class="fry"><span>Prawn cutlet</span><span>$1.80</span></div>
      <div class="fry"><span>Prawn twister</span><span>$3.00</span></div>
      <div class="fry"><span>Salt and pepper squid</span><span>$8.00</span></div>
      <div class="fry"><span>Sausage roll</span><span>$4.00</span></div>
      <div class="fry"><span>Sav shanty</span><span>$3.00</span></div>
      <div class="fry"><span>Seafood stick</span><span>$1.50</span></div>
      <div class="fry"><span>Spring roll - large</span><span>$3.00</span></div>
      <div class="fry"><span>Spring roll - mini</span><span>$1.50</span></div>
      <div class="fry"><span>Homemade vegetable patty</span><span>$3.50</span></div>
    </div>
  </div>

  <div class="panel burgers-panel">
    <div class="card burgers">
      <h2 class="bar-title head">Burgers and Sandwiches</h2>
      <div class="burger"><div><b>Classic Beef Burger</b><small>Meat patty, onion, lettuce, tomato &amp; beetroot</small></div><span class="price">$9.50</span></div>
      <div class="burger"><div><b>Big Rig Burger</b><small>Grilled chicken, meat patty, chicken schnitzel, onion, lettuce, tomato, beetroot, bacon, egg, cheese</small></div><span class="price">$7.50</span></div>
      <div class="burger"><div><b>The Beach Burger</b><small>Meat patty, onion, lettuce, tomato, grilled pineapple, bacon &amp; special mayo</small></div><span class="price">$11.00</span></div>
      <div class="burger"><div><b>B-Double Burger Stack</b><small>Meat patty, cheese, lettuce, tomato, egg, bacon, fried onion rings &amp; pickles</small></div><span class="price">$9.50</span></div>
      <div class="burger"><div><b>Outback Star Chicken</b><small>Grilled chicken, bacon, lettuce, tomato, honey garlic mayo</small></div><span class="price">$9.00</span></div>
      <div class="burger"><div><b>Tradies Schnity</b><small>Chicken schnitzel, lettuce &amp; mayo</small></div><span class="price">$8.00</span></div>
      <div class="burger"><div><b>Hair of the Dog</b><small>Grilled kransky, coleslaw, cheese, mustard, mayo and tomato sauce</small></div><span class="price">$8.00</span></div>
      <div class="burger"><div><b>From the Sea</b><small>Fish patty, lettuce, spanish onion, tomato &amp; tartare sauce</small></div><span class="price">$8.80</span></div>
      <div class="burger"><div><b>From the Bush</b><small>Homemade veggie patty, baby spinach, grilled veggies &amp; sweet chilli jam</small></div><span class="price">$12.50</span></div>
      <div class="burger"><div><b>Road Train Wrap</b><small>Sweet chilli tenders, lettuce, tomato, cheese, sweet chilli mayo</small></div><span class="price">$8.00</span></div>
      <div class="burger"><div><b>Shroom Burger</b><small>Grilled garlic and fresh field mushrooms, lettuce, tomato, pickles, pesto mayo</small></div><span class="price">$12.50</span></div>
      <div class="burger"><div><b>Steak It or Leave It</b><small>Daily special roast with gravy or mint sauce</small></div><span class="price">$7.50</span></div>
      <div class="burger"><div><b>Diesel Roast Roll</b><small>Daily special roast with gravy or mint sauce</small></div><span class="price">$7.50</span></div>
      <div class="burger"><div><b>DIY Sandwiches or Rolls</b><small>Add to a roll or fresh bread or a wrap: ham, chicken, lettuce, tomato, cucumber, carrot, cheese, cold roast, corned beef. Sauce: homemade chilli jam, mayo, chutney, tomato sauce, sweet chilli mayo, aioli</small></div></div>
    </div>
  </div>
</section>

</body>
</html>
```